Brochure Design for B-to-B software company

This project is for a product brochure in an 11x17 bifold format. The brochure will be a printed on heavy stock that will fold into 4 - 8 ½” x 11” pages. The folded edge will be on the left side. The brochure will be a combination of text and graphics. The completed editable files will be provided to us for further edits when needed. The color palette should complement and not overuse our logo colors.

Target Market(s)

Corporate Brands

Font styles to use
Sans Serif

Colors
cadf82

Requirements
Must have
• Color palette described in attached project overview document

```html
<!DOCTYPE html>
<html lang="en">
<head>
<meta charset="utf-8">
<title>Greenreach CRM Brochure Spread</title>
<link href="https://fonts.googleapis.com/css2?family=Bebas+Neue&family=Lato:wght@400;700&display=swap" rel="stylesheet">
<style>
  :root {
    --stage: #d6d6d6;
    --paper: #ffffff;
    --green-deep: #3f9a3c;
    --green-mid: #6cc24a;
    --green-light: #cadf82;
    --green-bright: #9fe46f;
    --text-dark: #333a3f;
    --text-body: #4a4f52;
    --box-line: #d5d5d5;
  }
  * { box-sizing: border-box; margin: 0; padding: 0; }
  html, body { width: 856px; height: 1200px; overflow: hidden; background: var(--stage); }
  .spread {
    position: absolute; left: 18px; top: 306px;
    width: 820px; height: 587px;
    background: var(--paper); overflow: hidden;
    font-family: "Lato", sans-serif;
  }
  .spread-art { position: absolute; inset: 0; width: 820px; height: 587px; }
  .brand-name {
    position: absolute; font-family: "Lato", sans-serif; font-weight: 700;
    white-space: nowrap; letter-spacing: 0.2px;
  }
  .brand-name--cover { left: 16px; top: 288px; font-size: 23px; color: #fff; }
  .brand-name--inside { left: 411px; top: 128px; font-size: 25px; color: var(--green-mid); }
  .contact { position: absolute; left: 16px; font-family: "Bebas Neue", sans-serif; color: #fff; white-space: nowrap; }
  .contact--phone { top: 372px; font-size: 22px; }
  .contact--web { top: 406px; font-size: 16px; letter-spacing: 0.3px; }
  .headline {
    position: absolute; left: 621px; top: 194px;
    font-family: "Bebas Neue", sans-serif; font-size: 22px; line-height: 21px;
    color: #fff;
  }
  .intro-title {
    position: absolute; left: 418px; top: 338px; width: 192px;
    text-align: center; font-size: 15.5px; line-height: 16px; color: var(--green-deep);
  }
  .intro-body {
    position: absolute; left: 418px; top: 374px; width: 192px;
    font-size: 5.9px; line-height: 6.6px; text-align: justify; color: var(--text-body);
  }
  .intro-body .accent { color: var(--green-mid); }
  .feature {
    position: absolute; height: 54px;
    border: 1px solid var(--box-line); border-radius: 5px;
    background: #fff; box-shadow: 0 1px 2px rgba(0,0,0,0.12);
    padding: 13px 6px 4px;
    font-size: 4.2px; line-height: 5.2px; color: var(--text-body);
  }
  .feature-title {
    position: absolute; left: -4px; right: -4px; top: -1px;
    background: var(--green-deep); color: #fff;
    font-size: 6px; line-height: 8px; text-align: center; border-radius: 1px;
  }
  .feature p + p { margin-top: 0; }
  .feature--branded { left: 480px; top: 458px; width: 122px; }
  .feature--orders { left: 614px; top: 458px; width: 121px; }
  .feature--pipeline { left: 418px; top: 520px; width: 122px; }
  .feature--compliance { left: 548px; top: 520px; width: 120px; }
  .feature--channel { left: 680px; top: 520px; width: 120px; }
</style>
</head>
<body>
<main class="spread">
  <svg class="spread-art" viewBox="0 0 820 587" xmlns="http://www.w3.org/2000/svg">
    <defs>
      <linearGradient id="coverGreen" x1="0" y1="0" x2="1" y2="1">
        <stop offset="0" stop-color="#8fe05f"/>
        <stop offset="0.5" stop-color="#6fcc4e"/>
        <stop offset="1" stop-color="#4fae43"/>
      </linearGradient>
      <linearGradient id="insideGreen" x1="0" y1="0" x2="0" y2="1">
        <stop offset="0" stop-color="#b3ef83"/>
        <stop offset="1" stop-color="#4f9f49"/>
      </linearGradient>
      <radialGradient id="leafGlow" cx="0.5" cy="0.5" r="0.5">
        <stop offset="0" stop-color="#a6ec74" stop-opacity="0.45"/>
        <stop offset="1" stop-color="#a6ec74" stop-opacity="0"/>
      </radialGradient>
      <linearGradient id="screenTone" x1="0" y1="0" x2="1" y2="1">
        <stop offset="0" stop-color="#f4f6f8"/>
        <stop offset="1" stop-color="#c9d2dc"/>
      </linearGradient>
    </defs>
    <rect x="0" y="0" width="410" height="587" fill="url(#coverGreen)"/>
    <rect x="410" y="0" width="410" height="587" fill="url(#insideGreen)"/>
    <rect class="cover-photo" x="0" y="120" width="400" height="380" fill="#3f8f3a" opacity="0.12" role="img" aria-label="Faded photo of banknotes and cannabis leaves"/>
    <rect class="inside-photo" x="560" y="0" width="260" height="300" fill="#3f8f3a" opacity="0.12" role="img" aria-label="Faded photo of a banknote and cannabis leaf"/>
    <path d="M0 0 H263 Q110 55 0 166 Z" fill="var(--paper)"/>
    <circle cx="397" cy="193" r="198" fill="var(--paper)"/>
    <path d="M172 587 C230 470 320 385 420 342 C480 318 520 300 560 296 L820 300 L820 587 Z" fill="var(--paper)"/>
    <circle cx="360" cy="200" r="150" fill="url(#leafGlow)" role="img" aria-label="Large leaf artwork"/>
    <rect x="616" y="320" width="185" height="123" rx="3" fill="url(#screenTone)" role="img" aria-label="Monitor and tablet showing a growth chart"/>
  </svg>

  <div class="brand-name brand-name--cover">Greenreach CRM</div>
  <div class="contact contact--phone">Phone +1 555-010-2244</div>
  <div class="contact contact--web">www.greenreachcrm.com</div>

  <div class="brand-name brand-name--inside">Greenreach CRM</div>

  <h1 class="headline">B-to-B Sales<br>Channel<br>Management<br>For the Cannabis<br>Industry</h1>

  <h2 class="intro-title">Accelerate Sales Growth<br>and Scale-up Quickly</h2>
  <p class="intro-body">Developing a B-to-B sales channel can dramatically increase sales growth that complements your retail, marketplace and distributor initiatives.<br>The <span class="accent">Greenreach</span> CRM B-to-B Sales Channel Management Solution is key to managing that growth and differentiating from competitors. Using our configurable and scalable sales portal CRM technology benefits both you and your customers.</p>

  <section class="feature feature--branded">
    <h3 class="feature-title">Branded Sales and CRM Portal</h3>
    <p>Launch quickly with your branding, products and content</p>
    <p>&nbsp;</p>
    <p>Allow approved retailers to place sales orders and access CoAs, marketing content and videos</p>
  </section>
  <section class="feature feature--orders">
    <h3 class="feature-title">Manage Orders Through Fulfillment</h3>
    <p>Manage products, discounts and inventory in easy-to-use dashboards</p>
    <p>Manage sales orders using automated workflow rules and notifications</p>
    <p>Direct orders to retailer locations</p>
    <p>Alert fulfillment teams as orders become ready for shipment</p>
  </section>
  <section class="feature feature--pipeline">
    <h3 class="feature-title">Pipeline and Sales Analytics</h3>
    <p>Track order status and pipeline with performance dashboards</p>
    <p>Analyze order and product sales trends</p>
    <p>View real-time key performance indicators (KPIs) for retailers</p>
  </section>
  <section class="feature feature--compliance">
    <h3 class="feature-title">Compliance and Tracking</h3>
    <p>&nbsp;</p>
    <p>Capture and track license status for retailer locations</p>
    <p>View audit trail for complete sales history</p>
    <p>Make CoAs available for download at any time</p>
  </section>
  <section class="feature feature--channel">
    <h3 class="feature-title">Grow and Manage Your Retail Sales Channel</h3>
    <p>Manage retailer leads</p>
    <p>Manage on-site marketing activities</p>
    <p>Manage Co-op marketing programs</p>
    <p>Track retailer performance</p>
  </section>
</main>
</body>
</html>
```